Brenwick Drilling Inc. Business card design

Business card design for "Brenwick Drilling Inc. - Directional Drilling Services"

Address is:

Brenwick Drilling Inc.
512 - 73 Tolvane Crescent SW
Calgary, Alberta, Canada
T2K 4P8

Please incorporate the logo design into the card, thank you.

Target Market(s)

Oil & Gas and Drilling

Industry/Entity Type

Business

```html
<!DOCTYPE html>
<html lang="en">
<head>
<meta charset="utf-8">
<title>Brenwick Drilling Inc. – Business Card</title>
<link rel="stylesheet" href="https://fonts.googleapis.com/css2?family=Arimo:wght@400;700&display=swap">
<style>
  :root {
    --backdrop: #ececec;
    --backdrop-edge: #dcdcdc;
    --card-white: #ffffff;
    --card-black: #000000;
    --brand-red: #c8262b;
    --ink-dark: #141414;
    --ink-light: #ffffff;
    --photo-light: #b9b9b9;
    --photo-dark: #3a3a3a;
  }
  * { box-sizing: border-box; margin: 0; padding: 0; }
  html, body { width: 1200px; height: 632px; overflow: hidden; }
  body {
    background: radial-gradient(ellipse at 50% 40%, var(--backdrop) 55%, var(--backdrop-edge) 100%);
    font-family: "Arimo", Arial, sans-serif;
    position: relative;
  }
  .card-pair {
    position: absolute;
    left: 70px;
    top: 150px;
    display: flex;
  }
  .card {
    width: 530px;
    height: 310px;
    position: relative;
    overflow: hidden;
  }
  .card-front { background: var(--card-white); }
  .card-back { background: var(--card-black); }
  .card-art { position: absolute; inset: 0; width: 100%; height: 100%; }

  .front-brand {
    position: absolute;
    left: 0; right: 0; top: 34px;
    display: flex; flex-direction: column; align-items: center;
  }
  .brand-mark {
    width: 76px; height: 76px;
    border-radius: 50%;
    border: 5px solid var(--brand-red);
    margin-bottom: 16px;
  }
  .brand-name {
    font-weight: 700;
    font-size: 23px;
    letter-spacing: 1.5px;
    color: var(--ink-dark);
    line-height: 1;
  }
  .brand-tagline {
    margin-top: 6px;
    font-weight: 700;
    font-size: 10.5px;
    letter-spacing: 3.1px;
    color: var(--ink-dark);
  }

  .back-photo {
    position: absolute; left: 0; top: 0;
    width: 290px; height: 100%;
    background: linear-gradient(160deg, var(--photo-light) 0%, #8a8a8a 45%, var(--photo-dark) 100%);
  }
  .back-brand {
    position: absolute; left: 282px; right: 0; top: 58px;
    display: flex; flex-direction: column; align-items: center;
  }
  .back-brand .brand-mark {
    width: 42px; height: 42px; border-width: 3px; margin-bottom: 8px;
  }
  .back-brand .brand-name { font-size: 13px; letter-spacing: 0.8px; color: var(--ink-light); }
  .back-brand .brand-tagline { font-size: 6px; letter-spacing: 1.7px; margin-top: 3px; color: var(--ink-light); }
  .back-address {
    position: absolute; left: 282px; right: 0; top: 196px;
    text-align: center;
    font-style: normal;
    font-size: 15px;
    line-height: 19px;
    color: var(--ink-light);
  }
</style>
</head>
<body>
  <main class="card-pair">
    <section class="card card-front" aria-label="Card front">
      <svg class="card-art" viewBox="0 0 530 310" preserveAspectRatio="none" aria-hidden="true">
        <path d="M0 245 C150 190 330 180 530 205 L530 310 L0 310 Z" fill="var(--brand-red)"/>
        <path d="M0 262 C160 205 340 196 530 212 L530 310 L0 310 Z" fill="var(--card-black)"/>
      </svg>
      <div class="front-brand">
        <span class="brand-mark" aria-hidden="true"></span>
        <span class="brand-name">BRENWICK DRILLING INC.</span>
        <span class="brand-tagline">DIRECTIONAL DRILLING SERVICES</span>
      </div>
    </section>

    <section class="card card-back" aria-label="Card back">
      <div class="back-photo" role="img" aria-label="Black and white photograph of a rig worker handling drill pipe on a drilling floor"></div>
      <svg class="card-art" viewBox="0 0 530 310" preserveAspectRatio="none" aria-hidden="true">
        <path d="M120 0 L175 0 C225 70 262 190 282 310 L268 310 C240 190 190 80 120 0 Z" fill="var(--brand-red)"/>
        <path d="M175 0 L530 0 L530 310 L282 310 C262 190 225 70 175 0 Z" fill="var(--card-black)"/>
      </svg>
      <div class="back-brand">
        <span class="brand-mark" aria-hidden="true"></span>
        <span class="brand-name">BRENWICK DRILLING INC.</span>
        <span class="brand-tagline">DIRECTIONAL DRILLING SERVICES</span>
      </div>
      <address class="back-address">
        Brenwick Drilling Inc.<br>
        512 - 73 Tolvane Crescent SW<br>
        Calgary, Alberta, Canada<br>
        T2K 4P8
      </address>
    </section>
  </main>
</body>
</html>
```